Bright Meadow LLC business card

I help with the Marketing and Sales of various Natural, Organic, Eco Friendly and Healthy Main Stream products to Retail Corporate accounts as well as Independents and Distributors.I also highlight Private label items to these same Retail Corporate accounts.Cherish the Moments, Enjoy Life!

Speciality & Health Sales and Marketing

Target Market(s)

Men and Women

Industry/Entity Type

Business

Contact Information for Business Card

Bright Meadow, LLC
Janet Lou Brindall
418 West Fern Lane
Ste 3-274
Phoenix, AZ 85047
602-555-0173
jbrindall@veltramail.net

Requirements
Must have
• Nice, femine font
Something in the background or on a side with a softness
Nice to have
• Cherish the Moments, Enjoy Life
Should not have
• Hardness

```html
<!DOCTYPE html>
<html lang="en">
<head>
<meta charset="utf-8">
<title>Bright Meadow LLC – Business Card</title>
<link rel="stylesheet" href="https://fonts.googleapis.com/css2?family=Cormorant+Garamond:ital,wght@0,500;0,600;1,500&family=Quicksand:wght@400;500&display=swap">
<style>
  :root {
    --page-bg: #e4e1de;
    --card-bg: #2a2628;
    --card-bg-soft: #3b3436;
    --accent: #f08a5d;
    --accent-soft: rgba(240, 138, 93, 0.22);
    --blush: rgba(246, 196, 178, 0.16);
    --text-light: #f7f1ee;
    --text-muted: #e2d8d4;
    --divider: rgba(247, 241, 238, 0.18);
  }
  * { box-sizing: border-box; margin: 0; padding: 0; }
  html, body {
    width: 1200px;
    height: 900px;
    overflow: hidden;
    background: var(--page-bg);
    font-family: "Quicksand", sans-serif;
  }
  .canvas {
    width: 1200px;
    height: 900px;
    display: flex;
    flex-direction: column;
    align-items: center;
    justify-content: center;
    gap: 44px;
  }
  .card {
    position: relative;
    width: 660px;
    height: 377px;
    border-radius: 18px;
    overflow: hidden;
    background:
      radial-gradient(ellipse 60% 90% at 0% 100%, var(--blush) 0%, transparent 70%),
      radial-gradient(ellipse 70% 70% at 45% 35%, var(--card-bg-soft) 0%, var(--card-bg) 75%);
    box-shadow: 0 10px 30px rgba(60, 40, 35, 0.18);
    color: var(--text-light);
  }
  .soft-glow {
    position: absolute;
    left: -90px;
    top: -60px;
    width: 320px;
    height: 320px;
    border-radius: 50%;
    background: radial-gradient(circle, var(--accent-soft) 0%, transparent 70%);
  }

  /* Front */
  .card-front {
    display: flex;
    flex-direction: column;
    align-items: center;
    justify-content: center;
    gap: 22px;
  }
  .brand-mark {
    width: 96px;
    height: 96px;
    border-radius: 50%;
    background: radial-gradient(circle at 35% 35%, #f6a882 0%, var(--accent) 70%);
  }
  .brand-name {
    position: relative;
    font-family: "Cormorant Garamond", serif;
    font-weight: 600;
    font-size: 50px;
    letter-spacing: 1px;
    color: var(--text-light);
  }

  /* Back */
  .card-back .identity {
    position: absolute;
    left: 44px;
    top: 66px;
  }
  .person-name {
    font-family: "Cormorant Garamond", serif;
    font-weight: 600;
    font-size: 36px;
    letter-spacing: 0.4px;
    line-height: 1.1;
  }
  .person-title {
    margin-top: 4px;
    font-family: "Cormorant Garamond", serif;
    font-style: italic;
    font-weight: 500;
    font-size: 20px;
    color: var(--accent);
  }
  .card-back .divider {
    position: absolute;
    left: 44px;
    right: 200px;
    top: 150px;
    height: 1px;
    background: linear-gradient(90deg, transparent, var(--divider) 20%, var(--divider) 80%, transparent);
  }
  .card-back .brand-mark {
    position: absolute;
    right: 64px;
    top: 44px;
    width: 116px;
    height: 116px;
  }
  .contact-list {
    position: absolute;
    right: 40px;
    bottom: 34px;
    list-style: none;
    font-size: 16px;
    font-weight: 500;
    line-height: 1.5;
    color: var(--text-muted);
  }
  .contact-list li {
    display: flex;
    justify-content: flex-end;
    align-items: center;
    gap: 10px;
  }
  .contact-icon {
    width: 14px;
    height: 14px;
    flex: none;
  }
  .icon-spacer { width: 14px; flex: none; }
  .contact-icon * {
    fill: none;
    stroke: var(--accent);
    stroke-width: 1.6;
    stroke-linecap: round;
    stroke-linejoin: round;
  }
</style>
</head>
<body>
<main class="canvas">
  <section class="card card-front" aria-label="Card front">
    <div class="soft-glow"></div>
    <div class="brand-mark"></div>
    <p class="brand-name">Bright Meadow LLC</p>
  </section>

  <section class="card card-back" aria-label="Card back">
    <div class="soft-glow"></div>
    <div class="identity">
      <p class="person-name">Janet Lou Brindall</p>
      <p class="person-title">Managing Director</p>
    </div>
    <div class="divider"></div>
    <div class="brand-mark"></div>
    <ul class="contact-list">
      <li>602.555.0173
        <svg class="contact-icon" viewBox="0 0 16 16" aria-hidden="true"><rect x="4" y="1.5" width="8" height="13" rx="2"/><line x1="7" y1="12" x2="9" y2="12"/></svg>
      </li>
      <li>418 West Fern Lane, Ste 3-274
        <svg class="contact-icon" viewBox="0 0 16 16" aria-hidden="true"><path d="M8 14.5s-4.5-4.5-4.5-8a4.5 4.5 0 0 1 9 0c0 3.5-4.5 8-4.5 8z"/><circle cx="8" cy="6.5" r="1.6"/></svg>
      </li>
      <li>Phoenix, AZ 85047<span class="icon-spacer"></span></li>
      <li>jbrindall@veltramail.net
        <svg class="contact-icon" viewBox="0 0 16 16" aria-hidden="true"><rect x="1.5" y="3.5" width="13" height="9" rx="1.5"/><polyline points="1.5,4.5 8,9 14.5,4.5"/></svg>
      </li>
      <li>www.brightmeadowllc.com
        <svg class="contact-icon" viewBox="0 0 16 16" aria-hidden="true"><path d="M7 9l2-2"/><path d="M6 6L4 8a2.5 2.5 0 0 0 4 4l2-2"/><path d="M10 10l2-2a2.5 2.5 0 0 0-4-4L6 6"/></svg>
      </li>
    </ul>
  </section>
</main>
</body>
</html>
```